Simplified minimalist but bold website

Design a website for a brand 'Brighten Each Morning' that shares ideas to make managing home and health easier through email swap series, webinars and eventually courses.

Simple landing page to attract users to sign up for a freebie.

Target Market(s)

women with families & homes to run

Number of Pages Required

1 page

Font styles to use
Sans Serif

Colors
e667a6
b768aa
acd136
ffffff
959595

Requirements
Must have
• Simplified look, line icons, opt-in template, contact us form

```html
<!DOCTYPE html>
<html lang="en">
<head>
<meta charset="utf-8">
<title>Brighten Each Morning</title>
<link rel="stylesheet" href="https://fonts.googleapis.com/css2?family=Alegreya+Sans:wght@300;400;500;700&family=Open+Sans:wght@400;600;700&display=swap">
<style>
:root{
  --plum:#b07aae;
  --plum-btn:#b768aa;
  --lilac:#e0c1e2;
  --lilac-field:#f3def5;
  --sky:#2fa6d6;
  --lime:#acd136;
  --white:#ffffff;
  --grey:#959595;
  --paper:#efefef;
  --ink:#333333;
}
*{box-sizing:border-box;margin:0;padding:0}
html,body{width:1200px;height:3130px;overflow:hidden}
body{position:relative;font-family:"Alegreya Sans",sans-serif;color:var(--white);background:var(--lilac)}
.abs{position:absolute}

/* nav */
.topbar{left:0;top:0;width:1200px;height:79px;background:var(--plum);z-index:2}
.nav{display:flex;gap:56px;position:absolute;right:60px;top:30px;font:700 15px "Open Sans",sans-serif;letter-spacing:.5px}

/* hero */
.hero{left:0;top:79px;width:1200px;height:721px}
.hero-photo{position:absolute;inset:0;background:linear-gradient(100deg,#d7b2dd 0%,#e6c9ea 45%,#f2e0ef 75%,#e9d2e6 100%)}
.hero h1{left:117px;top:208px;font-weight:300;font-size:46px;letter-spacing:1px;white-space:nowrap}
.hero p{left:117px;top:296px;font-weight:400;font-size:30px;white-space:nowrap}
.btn-outline{left:182px;top:378px;width:250px;height:59px;border:2px solid var(--white);border-radius:8px;display:flex;align-items:center;justify-content:center;font-size:18px;letter-spacing:1px}

/* help */
.help{left:0;top:800px;width:1200px;height:667px;background:var(--lilac)}
.section-title{font-weight:500;font-size:30px;letter-spacing:1.5px;width:100%;text-align:center}
.rule{width:56px;height:3px;background:var(--white)}
.col-note{font-size:15px;white-space:nowrap}
.col-title{font-size:26px;font-weight:400;width:500px;text-align:center}
.small-rule{width:80px;height:2px;background:var(--white)}
.body-text{font-size:17px;line-height:26px;text-align:center}
.field{width:303px;height:40px;background:var(--lilac-field);border-radius:4px;color:#c9a9c8;font-size:16px;display:flex;align-items:center;justify-content:center}
.btn-plum{width:303px;height:40px;background:var(--plum-btn);border-radius:4px;font:700 15px "Open Sans",sans-serif;display:flex;align-items:center;justify-content:center;letter-spacing:.5px}
.link{text-decoration:underline;font-size:18px;white-space:nowrap}

/* swap series */
.series{left:0;top:1467px;width:1200px;height:438px;background:var(--sky)}
.series .body-text{font-size:16px;line-height:22px}
.btn-lime{width:300px;height:40px;background:var(--lime);font:700 15px "Open Sans",sans-serif;display:flex;align-items:center;justify-content:center;border-radius:2px}

/* example + services */
.showcase{left:0;top:1905px;width:1200px;height:737px;background:var(--lilac)}
.label{font-size:16px}
.sample{left:109px;top:40px;width:482px;height:643px;background:var(--paper);color:var(--ink)}
.sample h3{position:absolute;left:0;top:14px;width:100%;font-weight:400;font-size:20px;text-align:center}
.sample-text{position:absolute;left:50px;width:400px;font:10.5px/15px "Open Sans",sans-serif}
.product{position:absolute;top:55px;height:90px;border-radius:6px}
.box{position:absolute;width:190px;background:var(--white);border:1px solid #d2d2d2;font:9.5px/13px "Open Sans",sans-serif;color:#555;overflow:hidden}
.box-head{background:#e6e6e6;color:var(--plum-btn);text-align:center;font-size:11px;padding:4px 0}
.box-body{padding:6px 8px}
.box-body .big{text-align:center;font-size:12px;margin-bottom:4px}
.guide{position:absolute;left:52px;top:578px;width:388px;background:var(--white);border:1px solid #d2d2d2;font:10px "Open Sans",sans-serif}
.guide .box-head{text-align:left;padding-left:8px}
.guide .guide-link{padding:7px 8px;color:#3b6fc4}
.price-panel{left:680px;top:95px;width:380px;height:162px;background:rgba(255,255,255,.35)}
.cell{position:absolute;width:98px;height:32px;background:var(--white);border:2px solid var(--plum-btn);color:var(--plum-btn);font-size:13px;display:flex;align-items:center;justify-content:center;white-space:nowrap}
.results{left:838px;top:297px;font-size:20px;font-weight:700}
.photo{position:absolute;border-radius:2px}
.tag{font-size:17px;font-weight:700}

/* contact */
.contact{left:0;top:2642px;width:1200px;height:388px;background:var(--sky)}
.input{position:absolute;width:301px;height:40px;background:var(--paper);color:var(--grey);font-size:16px;padding:10px 12px}
.send{left:190px;top:310px;width:301px;height:40px;background:var(--lime);font-size:18px;letter-spacing:1px;display:flex;align-items:center;justify-content:center}

/* footer */
.footer{left:0;top:3030px;width:1200px;height:100px;background:var(--plum);font-size:16px}
.footer .item{top:50%;transform:translateY(-50%);display:flex;align-items:center;gap:9px;white-space:nowrap}
.footer .links{font:700 14px "Open Sans",sans-serif;gap:40px}
.social{width:26px;height:26px;border-radius:50%;background:var(--white)}
</style>
</head>
<body>

<header class="abs topbar">
  <nav class="nav"><span>HOME</span><span>ABOUT</span><span>BLOG</span><span>CONTACT</span></nav>
</header>

<section class="abs hero">
  <div class="hero-photo" role="img" aria-label="Flat-lay photo of a cup of tea, sugar cubes in a glass bowl, a spoon and sprigs of white baby's breath on a lilac surface"></div>
  <h1 class="abs">Brighten Each Morning</h1>
  <p class="abs">Chances are life is a little overwhelming … Let us help</p>
  <div class="abs btn-outline">LEARN MORE</div>
</section>

<section class="abs help">
  <h2 class="abs section-title" style="top:50px">HOW WE HELP ?</h2>
  <div class="abs rule" style="left:572px;top:107px"></div>

  <div class="abs col-note" style="left:108px;top:128px">Baby Steps… (try out a few of our tricks)</div>
  <div class="abs col-note" style="left:618px;top:124px">Big Leap… (I'm ready to roll up my sleeves)</div>

  <div class="abs col-title" style="left:99px;top:175px">Swaps Email Series</div>
  <div class="abs small-rule" style="left:309px;top:222px"></div>
  <div class="abs body-text" style="left:60px;top:235px;width:580px">Save TIME, MONEY and SANITY with simple product swaps.</div>
  <div class="abs body-text" style="left:100px;top:278px;width:500px;font-size:15px;line-height:23px">Reduce the amount of work it takes to run your home.<br>Swap out existing products for more sustainable ones.<br>Each swap saves you work, clutter, time &amp; money.</div>
  <div class="abs link" style="left:187px;top:372px">SEE SAMPLE SWAP</div>
  <div class="abs link" style="left:401px;top:372px">LEARN MORE</div>

  <div class="abs body-text" style="left:198px;top:432px;width:303px;font-weight:700">Send your ideas my way…</div>
  <div class="abs field" style="left:198px;top:471px">Name</div>
  <div class="abs field" style="left:198px;top:531px">Email</div>
  <div class="abs btn-plum" style="left:198px;top:586px">SEND ME THE GUIDE!</div>

  <div class="abs col-title" style="left:599px;top:175px">Decluttering Guide</div>
  <div class="abs small-rule" style="left:809px;top:222px"></div>
  <div class="abs" role="img" aria-label="Illustration of two tilted white guide cards" style="left:695px;top:240px;width:310px;height:220px;background:linear-gradient(160deg,rgba(255,255,255,.45),rgba(255,255,255,.2));border-radius:4px"></div>
  <div class="abs field" style="left:699px;top:471px">Name</div>
  <div class="abs field" style="left:699px;top:531px">Email</div>
  <div class="abs btn-plum" style="left:699px;top:586px">SIGN ME UP!</div>
</section>

<section class="abs series">
  <h2 class="abs section-title" style="top:48px">SWAP EMAIL SERIES</h2>
  <div class="abs rule" style="left:572px;top:105px"></div>
  <div class="abs body-text" style="left:200px;top:125px;width:800px">Save TIME, MONEY and SANITY with simple product swaps.<br>And reduce the amount of work it takes to run your home.<br>Swap out existing products for more sustainable ones.<br>Each swap save you work, clutter, time &amp; money</div>
  <div class="abs body-text" style="left:200px;top:225px;width:800px">You get an email 2x weekly for 6-12 weeks only<br>Get even more if you feel they are helpful to you</div>
  <div class="abs body-text" style="left:200px;top:288px;width:800px">Join our monthly SIMPLE SWAP SHARING web jams with other mums and get even more ideas.<br>Better yet, come with great tips of your own to share.</div>
  <div class="abs btn-lime" style="left:449px;top:357px">SIGN ME UP!</div>
</section>

<section class="abs showcase">
  <div class="abs label" style="left:109px;top:13px">Swap Email Example</div>
  <div class="abs label" style="left:620px;top:13px">Organizing Services</div>

  <div class="abs sample">
    <h3>Mouthwash for Tongue Scraper</h3>
    <div class="product" role="img" aria-label="Photo of a blue mouthwash bottle" style="left:140px;width:56px;background:linear-gradient(#7fc9e2,#2e8fb8)"></div>
    <div class="product" role="img" aria-label="Drawing of a tongue scraper" style="left:285px;width:34px;background:linear-gradient(#c9d6ea,#8fa6cc)"></div>
    <p class="sample-text" style="left:50px;top:158px;font-weight:600">Tongue scrapers/cleaners are plastic or metal gadgets with arcs that help scrap off all the white stuff (bacteria) that gathered on your tongue in the morning.</p>
    <p class="sample-text" style="left:50px;top:208px">The bacteria is responsible for most bad breath. So, if you use mouthwash to freshen your breath, use a scraper before brushing your teeth.</p>

    <div class="box" style="left:52px;top:270px;height:113px">
      <div class="box-head">Clutter Savings</div>
      <div class="box-body"><div class="big">Plastic Bottle</div>One less bulky bottle under the sink. A scraper makes almost no waste and lasts for years.</div>
    </div>
    <div class="box" style="left:250px;top:270px;height:113px">
      <div class="box-head">Time Savings</div>
      <div class="box-body"><div class="big">7-10 mins / Month</div>Less time buying, storing and recycling mouthwash. One trip a year at most.</div>
    </div>
    <div class="box" style="left:52px;top:404px;height:150px">
      <div class="box-head">Cost Savings</div>
      <div class="box-body"><div class="big">$5-10 / Month</div>Removes a monthly expense. A scraper costs a few dollars. Pick one that reaches the whole tongue, not the little brush kind.</div>
    </div>
    <div class="box" style="left:250px;top:404px;height:150px">
      <div class="box-head">Other Benefits</div>
      <div class="box-body">Easy to travel with and add to your daily routine.<br>Environmentally conscious.<br>No harmful chemicals.</div>
    </div>
    <div class="guide">
      <div class="box-head">Buying Guide</div>
      <div class="guide-link">Tongue Scrapers / Scrubbers on Shopwell</div>
    </div>
  </div>

  <div class="abs price-panel"></div>
  <div class="cell" style="left:697px;top:82px">First 1 hour</div>
  <div class="cell" style="left:818px;top:77px">Intake</div>
  <div class="cell" style="left:939px;top:82px;font-size:10.5px">$50 (first hour only)</div>
  <div class="cell" style="left:697px;top:130px">1 hour</div>
  <div class="cell" style="left:939px;top:130px">$75</div>
  <div class="cell" style="left:697px;top:185px">3 hours</div>
  <div class="cell" style="left:818px;top:185px">1 session</div>
  <div class="cell" style="left:939px;top:185px">$200</div>
  <div class="cell" style="left:697px;top:238px">5 hours</div>
  <div class="cell" style="left:818px;top:238px">1-2 sessions</div>
  <div class="cell" style="left:939px;top:238px">$300</div>

  <div class="abs results">Results</div>
  <div class="abs tag" style="left:643px;top:412px">Before</div>
  <div class="photo" role="img" aria-label="Photo of a cluttered closet before organizing" style="left:805px;top:362px;width:282px;height:136px;background:linear-gradient(90deg,#5a4a56,#8a6d7a,#c3b7bd)"></div>
  <div class="abs tag" style="left:647px;top:588px">After</div>
  <div class="photo" role="img" aria-label="Photo of an organized wardrobe after organizing" style="left:716px;top:510px;width:370px;height:182px;background:linear-gradient(90deg,#7a5a48,#b59a86,#8f6f62)"></div>
</section>

<section class="abs contact">
  <h2 class="abs section-title" style="top:45px">CONTACT US</h2>
  <div class="abs rule" style="left:572px;top:103px"></div>
  <div class="input" style="left:190px;top:133px">Name *</div>
  <div class="input" style="left:190px;top:192px">Email *</div>
  <div class="input" style="left:190px;top:251px">Subject</div>
  <div class="input" style="left:511px;top:133px;width:501px;height:158px">Message</div>
  <div class="abs send">SEND</div>
</section>

<footer class="abs footer">
  <span class="abs item" style="left:118px">Mara Elling</span>
  <span class="abs item" style="left:236px">
    <svg width="24" height="24" viewBox="0 0 24 24" aria-hidden="true"><path fill="#fff" d="M6.6 10.8a15.1 15.1 0 0 0 6.6 6.6l2.2-2.2a1 1 0 0 1 1-.25 11.4 11.4 0 0 0 3.6.57 1 1 0 0 1 1 1V20a1 1 0 0 1-1 1A17 17 0 0 1 3 4a1 1 0 0 1 1-1h3.5a1 1 0 0 1 1 1c0 1.25.2 2.46.57 3.6a1 1 0 0 1-.25 1z"/></svg>
    555.014.2290</span>
  <span class="abs item" style="left:384px">
    <svg width="26" height="18" viewBox="0 0 28 20" aria-hidden="true"><rect x="1" y="1" width="26" height="18" fill="none" stroke="#fff" stroke-width="2"/><path d="M1 1l13 10L27 1" fill="none" stroke="#fff" stroke-width="2"/></svg>
    hello@brightmorning.co</span>
  <span class="abs item" style="left:612px"><span class="social"></span>Friendbook</span>
  <span class="abs item links" style="left:760px"><span>HOME</span><span>ABOUT</span><span>BLOG</span><span>CONTACT</span></span>
</footer>

</body>
</html>
```